New corporate stationery design for UK train leasing company

In advance of an office move later this year we are looking to redesign all our corporate stationery (business cards, letterhead, compliment slips, envelopes etc) as well as small branded items (such as mouse mats, drink mats, etc).

We wish to keep the same logo and corporate colours but are looking for a modern, fresh look that will tie in our stationery more with the look of our website and our PowerPoint template. We have a strapline, "Track Crews, True Knowhow" that we would like to incorporate into the stationery design and also need to include a "TEMLO" logo on the bottom of the letterhead/compliment slips. We have two offices so will need letterhead and compliment slips with both addresses.

The files attached include different versions of our logo (the main one is the black with green halo, file 1 or 3), our brand guidelines summary (including Pantone colours), the TEMLO logo and PowerPoint template.

More information about the business can be found at www.fernholtrail.co.uk.

If you have any questions please let me know.

I look forward to seeing the designs!
Regards
Moira

Target Market(s)

Main audience are train operators, rail industry suppliers, passenger transport groups, government and other political organisations, financiers/lenders.

Industry/Entity Type

Business

```html
<!DOCTYPE html>
<html lang="en">
<head>
<meta charset="utf-8">
<title>Fernhol Rail – Business Card</title>
<link href="https://fonts.googleapis.com/css2?family=Open+Sans:wght@300;400;600&display=swap" rel="stylesheet">
<style>
  :root {
    --page-bg: #efefef;
    --teal: #3fae9a;
    --teal-deep: #369a88;
    --teal-soft: #5cc0ad;
    --card-white: #ffffff;
    --ink: #3a3d3f;
    --ink-soft: #6f7476;
  }
  * { box-sizing: border-box; margin: 0; padding: 0; }
  html, body {
    width: 1200px; height: 1000px; overflow: hidden;
    background: var(--page-bg);
    font-family: "Open Sans", Arial, sans-serif;
  }
  .stationery {
    position: absolute; inset: 0;
    display: flex; align-items: center; justify-content: center; gap: 60px;
  }
  .card {
    position: relative; width: 470px; height: 300px; overflow: hidden;
    box-shadow: 0 6px 18px rgba(0,0,0,0.12);
  }
  .card-front { background: var(--teal); }
  .card-art { position: absolute; inset: 0; width: 100%; height: 100%; }
  .brand-front {
    position: absolute; left: 0; right: 0; top: 122px; text-align: center;
    color: var(--card-white); font-weight: 300; font-size: 44px; letter-spacing: 1px;
  }
  .card-back { background: var(--card-white); }
  .brand-back {
    position: absolute; left: 34px; top: 40px;
    color: var(--ink); font-weight: 300; font-size: 24px;
  }
  .contact { position: absolute; left: 34px; top: 98px; color: var(--ink); }
  .contact-name { font-size: 17px; font-weight: 400; }
  .contact-role { font-size: 12px; font-weight: 400; margin-bottom: 10px; }
  .contact-line { display: flex; align-items: center; gap: 7px; font-size: 9.5px; color: var(--ink-soft); line-height: 16px; }
  .contact-line svg { width: 9px; height: 9px; fill: var(--teal); flex: none; }
  .offices { position: absolute; right: 30px; top: 30px; width: 160px; font-size: 8.5px; line-height: 12px; color: var(--ink-soft); }
  .office-label { color: var(--teal); font-weight: 600; }
  .office + .office { margin-top: 8px; }
</style>
</head>
<body>
<main class="stationery">
  <section class="card card-front" aria-label="Business card front">
    <svg class="card-art" viewBox="0 0 470 300" preserveAspectRatio="none" aria-hidden="true">
      <path d="M0 230 C150 180 320 150 470 40 L470 0 L0 0 Z" fill="var(--teal-soft)" opacity="0.25"/>
      <path d="M0 300 C160 240 330 210 470 110 L470 300 Z" fill="var(--teal-deep)" opacity="0.35"/>
    </svg>
    <div class="brand-front">Fernhol Rail</div>
  </section>

  <section class="card card-back" aria-label="Business card back">
    <svg class="card-art" viewBox="0 0 470 300" preserveAspectRatio="none" aria-hidden="true">
      <path d="M0 300 L0 268 C170 258 330 190 470 90 L470 300 Z" fill="var(--teal)"/>
      <path d="M0 268 C170 258 330 190 470 90 L470 112 C330 210 170 272 0 282 Z" fill="var(--teal-soft)"/>
    </svg>
    <div class="brand-back">Fernhol Rail</div>
    <div class="contact">
      <p class="contact-name">Daniel Hart</p>
      <p class="contact-role">Managing Director</p>
      <p class="contact-line">
        <svg viewBox="0 0 10 10"><path d="M2 0.5 L3.8 2.6 L2.9 3.8 C3.6 5.2 4.8 6.4 6.2 7.1 L7.4 6.2 L9.5 8 L8.4 9.5 C4.4 9.2 0.8 5.6 0.5 1.6 Z"/></svg>
        +44 (0) 20 7946 0321
      </p>
      <p class="contact-line">
        <svg viewBox="0 0 10 10"><path d="M0 2 H10 V8 H0 Z M0.8 2.6 L5 5.6 L9.2 2.6"/></svg>
        communications@fernholtrail.co.uk
      </p>
      <p class="contact-line">
        <svg viewBox="0 0 10 10"><circle cx="5" cy="5" r="5"/></svg>
        www.fernholtrail.co.uk
      </p>
    </div>
    <div class="offices">
      <div class="office">
        <p class="office-label">Head Office</p>
        <p>Harrow Court, Vale Street,<br>London SE1 4QT</p>
      </div>
      <div class="office">
        <p class="office-label">Second Office</p>
        <p>5 Mill Yard, Riverside Park,<br>Derby DE24 8UP</p>
      </div>
    </div>
  </section>
</main>
</body>
</html>
```